Brell Harbor Company Business Cards

Front and Back Business Card - logo and text setup - cool design. I need workable photoshop or illustrator files so I can setup each employee card with design that is created
Updates

Hi everyone, thank you for the great entries. Please no more white and blue cards - there are so many already - black and silver only now please. thanks!

Target Market(s)

Construction Industry - Facility Managers

Industry/Entity Type

Construction

Contact Information for Business Card

I really like contemporary simplistic looks - clean neat....not opposed to seeing some black backrounds

Requirements
Must have
• Logo/website address with design on front only - www.brellharbor-example.com (logo attached)
• Back:
• Name/Title/Company Address/Phone/email address
Nice to have
• Cool design
Should not have
• Nothing gimmicky like Fire or Water - since we are a Fire Protection company - it has all been done

```html
<!DOCTYPE html>
<html lang="en">
<head>
<meta charset="utf-8">
<title>Brell Harbor Company Business Cards</title>
<link rel="stylesheet" href="https://fonts.googleapis.com/css2?family=Jost:wght@300;400;500;700&family=Open+Sans:ital,wght@0,400;1,400&display=swap">
<style>
  :root {
    --orange: #ef4934;
    --navy: #263f74;
    --card-grey: #dedfe1;
    --card-black: #05090b;
    --page: #ebebeb;
    --white: #ffffff;
  }
  * { margin: 0; padding: 0; box-sizing: border-box; }
  html, body { width: 1200px; height: 1200px; overflow: hidden; }
  body {
    background: var(--page);
    position: relative;
    font-family: "Jost", sans-serif;
  }
  .card {
    position: absolute;
    border-radius: 12px;
    overflow: hidden;
  }
  /* Front */
  .card-front {
    left: 262px; top: 172px; width: 672px; height: 384px;
    background: var(--card-black);
  }
  .front-brand {
    position: absolute; left: 0; right: 0; top: 134px;
    text-align: center;
  }
  .front-brand .company-name {
    font-family: "Jost", sans-serif;
    font-weight: 700;
    font-size: 58px;
    line-height: 1;
    color: var(--navy);
    letter-spacing: -0.5px;
  }
  .front-brand .website {
    margin-top: 14px;
    font-family: "Open Sans", sans-serif;
    font-style: italic;
    font-size: 21px;
    color: var(--orange);
  }
  /* Back */
  .card-back {
    left: 254px; top: 660px; width: 674px; height: 386px;
    background: var(--card-grey);
  }
  .back-brand {
    position: absolute; left: 30px; top: 30px;
    font-weight: 700; font-size: 30px; line-height: 1;
    color: var(--navy);
  }
  .holder {
    position: absolute; right: 26px; top: 24px;
    text-align: right;
  }
  .holder .name {
    font-weight: 500; font-size: 40px; line-height: 1;
    color: var(--orange);
  }
  .holder .title {
    margin-top: 4px;
    font-weight: 400; font-size: 21px;
    color: var(--navy);
  }
  .contact-band {
    position: absolute; left: 0; right: 0; top: 212px; bottom: 0;
    background: var(--orange);
    border-top: 3px solid var(--navy);
  }
  .address {
    position: absolute; left: 0; right: 0; top: 6px;
    text-align: center;
    font-weight: 300; font-size: 20px;
    color: var(--white);
  }
  .contact-line {
    position: absolute; bottom: 52px;
    display: flex; align-items: center; gap: 6px;
    font-family: "Open Sans", sans-serif;
    font-size: 16px;
    color: var(--white);
  }
  .contact-line.phone { left: 37px; }
  .contact-line.email { right: 26px; }
  .contact-line svg { display: block; }
</style>
</head>
<body>
  <section class="card card-front">
    <div class="front-brand">
      <div class="company-name">Brell Harbor</div>
      <div class="website">www.brellharbor-example.com</div>
    </div>
  </section>

  <section class="card card-back">
    <div class="back-brand">Brell Harbor</div>
    <div class="holder">
      <div class="name">Mara Lindqvist</div>
      <div class="title">Managing Director</div>
    </div>
    <div class="contact-band">
      <div class="address">Company Address: Your address</div>
      <div class="contact-line phone">
        <svg width="26" height="20" viewBox="0 0 26 20" aria-hidden="true">
          <path d="M2 7 C2 2 24 2 24 7 L24 9 L18 9 L18 6 L8 6 L8 9 L2 9 Z" fill="var(--navy)"/>
          <path d="M6 10 L20 10 L24 19 L2 19 Z" fill="var(--navy)"/>
          <circle cx="13" cy="14" r="3" fill="var(--orange)"/>
        </svg>
        <span>555 0142 7788</span>
      </div>
      <div class="contact-line email">
        <svg width="30" height="20" viewBox="0 0 30 20" aria-hidden="true">
          <rect x="1" y="1" width="28" height="18" fill="var(--navy)"/>
          <path d="M2 2 L15 12 L28 2" fill="none" stroke="var(--orange)" stroke-width="1.6"/>
        </svg>
        <span>info@brellharbor-example.com</span>
      </div>
    </div>
  </section>
</body>
</html>
```